Visitenkarten-Design für Forschungs- und Beratungsunternehmen
Zielgruppe
*Veridora' ist ein Forschungs- und Beratungsunternehmen für Lebensmittelwirkungen. Unsere Angebote sind: Vorträge, Workshops, Seminare und Coaching. Die Zielgruppen sind Pädagogen, Mediziner, Psychologen u.a.m.
Aufgabenstellung
Bei Bedarf kann die Gestaltung der Visitenkarte auch auf die Rückseite ausgedehnt werden.

```html
<!DOCTYPE html>
<html lang="de">
<head>
<meta charset="utf-8">
<title>Veridora – Visitenkarte</title>
<link rel="stylesheet" href="https://fonts.googleapis.com/css2?family=Montserrat:wght@600&family=Open+Sans:wght@400;700&display=swap">
<style>
  :root {
    --bg: #2e2e30;
    --card-dark: #2b2b2b;
    --paper: #ffffff;
    --brand-blue: #1a7cc6;
    --ink: #2a2a2a;
    --orange: #f2a516;
    --green: #7cbf3a;
    --pink: #d63a8f;
    --white: #ffffff;
  }
  html, body {
    margin: 0;
    width: 1200px;
    height: 970px;
    overflow: hidden;
    background: var(--bg);
  }
  .canvas {
    position: relative;
    width: 1200px;
    height: 970px;
  }
  .card {
    position: absolute;
    left: 270px;
    width: 660px;
    height: 390px;
    overflow: hidden;
    box-shadow: 0 12px 30px rgba(0,0,0,.45);
  }
  .card--front { top: 70px; background: var(--card-dark); }
  .card--back { top: 510px; background: var(--paper); }
  .card svg { display: block; }
  .brand {
    font-family: "Montserrat", sans-serif;
    font-weight: 600;
    fill: var(--brand-blue);
    letter-spacing: 2px;
  }
  .contact { font-family: "Open Sans", sans-serif; fill: var(--ink); font-size: 14px; }
  .contact__name { font-weight: 700; fill: var(--brand-blue); font-size: 22px; }
  .contact__role { font-size: 13px; }
  .hours { font-family: "Open Sans", sans-serif; fill: var(--white); font-size: 14px; }
  .icon { fill: var(--brand-blue); }
</style>
</head>
<body>
<main class="canvas">

  <section class="card card--front" aria-label="Vorderseite">
    <svg width="660" height="390" viewBox="0 0 660 390">
      <circle cx="190" cy="195" r="20" fill="var(--brand-blue)"/>
      <text class="brand" x="230" y="213" font-size="50">VERIDORA</text>
    </svg>
  </section>

  <section class="card card--back" aria-label="Rückseite">
    <svg width="660" height="390" viewBox="0 0 660 390">
      <defs>
        <linearGradient id="accent-fill" x1="0" y1="0" x2="1" y2="0">
          <stop offset="0" stop-color="var(--pink)"/>
          <stop offset="0.35" stop-color="var(--orange)"/>
          <stop offset="0.7" stop-color="var(--green)"/>
          <stop offset="1" stop-color="var(--brand-blue)"/>
        </linearGradient>
      </defs>

      <rect class="accent-strip" x="0" y="312" width="660" height="8" fill="url(#accent-fill)" role="img" aria-label="Farbige Akzentlinien in Pink, Orange, Grün und Blau"/>
      <rect class="footer-band" x="0" y="320" width="660" height="70" fill="var(--card-dark)"/>
      <text class="hours" x="630" y="360" text-anchor="end">MO - FR 10.00 - 18.00 h</text>

      <circle cx="65" cy="205" r="13" fill="var(--brand-blue)"/>
      <text class="brand" x="86" y="216" font-size="30">VERIDORA</text>

      <line x1="315" y1="90" x2="315" y2="260" stroke="var(--brand-blue)" stroke-width="2"/>

      <text class="contact contact__name" x="340" y="100">Lukas Berendt</text>
      <text class="contact contact__role" x="340" y="120">Nutrition Research / Consulting</text>
      <text class="contact" x="340" y="152">Lindenweg 14</text>
      <text class="contact" x="340" y="170">CH-4153 Reinach</text>

      <g class="icon">
        <path d="M343,191 q0,-3 3,-3 l2,0 l2,4 l-2,2 q2,4 5,5 l2,-2 l4,2 l0,2 q0,3 -3,3 q-13,-2 -13,-13 z"/>
        <path d="M342,211 h15 v10 h-15 z M342,211 l7.5,6 l7.5,-6" fill="none" stroke="var(--brand-blue)" stroke-width="1.8"/>
        <circle cx="349.5" cy="236" r="7" fill="none" stroke="var(--brand-blue)" stroke-width="1.8"/>
        <path d="M342.5,236 h14 M349.5,229 q-5,7 0,14 q5,-7 0,-14" fill="none" stroke="var(--brand-blue)" stroke-width="1.4"/>
      </g>
      <text class="contact" x="367" y="200">+41 61 555 24 90</text>
      <text class="contact" x="367" y="221">info@veridora.ch</text>
      <text class="contact" x="367" y="242">www.veridora.ch</text>
    </svg>
  </section>

</main>
</body>
</html>
```